Health Wellbeing Beauty online Shop

I have attached a full spec, however in summary this is a new business startup selling skincare products.

We need a web design for new wellbeing website, selling skincare products so need an eCommerce solution . On the home page I would like these faces to dissolve into each other on a loop or use a honeycomb style transation.
You will need the option of being able to log into an account, either through chatterbook, quorvix, tweedle or create an account. For created accounts, obviously need the facility to be able to reset passwords, see previous orders, track current order, and maintain favourites.
It should be PC, mobile and tablet friendly.

Look and Feel
It should be an elegant, modern, professional, trendy, unisex website. It should look clean and calm. Am happy to try interesting and slightly unusual designs. I would also like to have chat functionality, either powered by morvaLKtalk or by Quo 81.
Websites I like are
https://www.noble-radiance.example.co.uk/
https://www.onlyminerals.example.co.uk/
http://www.claramedica.example.com/

PLEASE DO USE YOUR KNOWELDGE OF WHAT WORKS FOR WEB DESIGN. YOU’RE THE EXPERT AND NEED YOUR EXPERTISE. CARTE BLANCHE TO DESIGN AS YOU SEE FIT. Please be creative, I need my site to stand out from the crowd.

Target Market(s)

Target Market
Middle aged women are our most common client, however, younger patients, both male and female, will often visit the site. In summary, I would like the site to appeal to all age brackets.

Requirements
Must have
• Need shop to be exactly like shop on this link http://www.claramedica.example.com/
Nice to have
• i would like something unique and creative

```html
<!DOCTYPE html>
<html lang="en">
<head>
<meta charset="utf-8">
<title>Lumea — Health, Wellbeing, Beauty</title>
<link rel="stylesheet" href="https://fonts.googleapis.com/css2?family=Open+Sans:wght@400;600;700;800&display=swap">
<style>
:root{
  --ink:#333;
  --muted:#888;
  --line:#e2e2e2;
  --dark:#1f1f1f;
  --dark-2:#2b2b2b;
  --green:#7ab51d;
  --orange:#f39c12;
  --gold:#f5b800;
  --red:#d9302c;
  --paper:#fff;
  --soft:#f6f6f6;
}
*{box-sizing:border-box;margin:0;padding:0}
html,body{width:753px;height:1200px;overflow:hidden;background:var(--paper)}
body{font-family:"Open Sans",Arial,sans-serif;color:var(--ink);font-size:8px;position:relative}
ul{list-style:none}

/* top bar */
.topbar{height:20px;background:var(--dark);color:#ddd;display:flex;justify-content:space-between;align-items:center;padding:0 14px;font-size:7px;letter-spacing:.3px}
.topbar .links span{margin-left:10px}
.topbar .links span+span:before{content:"|";margin-right:10px;color:#666}

/* header */
.header{height:86px;display:flex;align-items:center;padding:0 14px;position:relative}
.brand{display:flex;align-items:center;gap:8px;width:200px}
.brand-dot{width:34px;height:34px;border-radius:50%;border:2px solid #555}
.brand-name{font-size:18px;font-weight:600;color:#444;letter-spacing:1px}
.shipping{position:absolute;left:300px;top:22px;text-align:center}
.shipping b{display:block;font-size:8.5px;font-weight:700;letter-spacing:.3px}
.shipping small{font-size:6.5px;color:var(--muted)}
.shipping svg{position:absolute;left:-22px;top:0}
.search{position:absolute;right:14px;top:24px;display:flex;width:170px;height:18px;border:1px solid var(--line)}
.search span{flex:1;font-size:7px;color:#aaa;padding:4px 6px}
.search i{width:20px;background:var(--gold);display:flex;align-items:center;justify-content:center}

/* nav */
.nav{position:absolute;top:108px;left:12px;right:8px;height:22px;border:1px solid var(--line);display:flex;align-items:center}
.nav .cat-btn{width:165px;height:100%;background:var(--dark);color:#fff;font-weight:700;font-size:8px;display:flex;align-items:center;justify-content:space-between;padding:0 8px}
.nav .menu{display:flex}
.nav .menu a{padding:0 12px;font-size:7.5px;font-weight:700;color:var(--ink);text-decoration:none;border-right:1px solid var(--line);line-height:20px}
.nav .cart{margin-left:auto;padding-right:8px;font-size:7px;display:flex;align-items:center;gap:4px}

/* sidebar */
.sidebar{position:absolute;left:12px;top:130px;width:165px}
.cat-list{background:var(--dark-2);padding:4px 0;height:146px}
.cat-list li{color:#eee;font-size:7px;padding:4px 8px;border-bottom:1px solid #3a3a3a}
.cat-list li:first-child{color:var(--green)}
.block{margin-top:14px}
.block-title{font-size:8px;font-weight:700;padding-bottom:4px;border-bottom:1px solid var(--line);margin-bottom:6px}
.shop-by{border:1px solid var(--line);padding:6px;height:162px;margin-top:20px}
.shop-by h5{font-size:7.5px;background:var(--soft);padding:3px 4px;margin:4px 0}
.shop-by p{font-size:6.5px;color:#555;padding:2px 4px}
.promo{margin-top:12px;height:138px;border:1px solid var(--line);position:relative;overflow:hidden}
.promo .art{position:absolute;inset:0;background:linear-gradient(180deg,#fbfbfb 0%,#f3ede4 60%,#e7d7c1 100%)}
.promo h4{position:relative;font-size:13px;font-weight:400;color:#555;padding:8px 8px 2px}
.promo p{position:relative;font-size:5.5px;color:#777;padding:0 8px}
.mini{display:flex;gap:6px;margin-bottom:8px}
.mini .thumb{width:28px;height:36px;background:linear-gradient(180deg,#f4f4f4,#dedede)}
.mini .thumb.amber{background:linear-gradient(180deg,#a47a5c,#6b4128)}
.mini b{display:block;font-size:6.5px;font-weight:600}
.mini em{font-style:normal;font-size:7px;color:var(--red);font-weight:700}
.mini small{display:block;font-size:6px;color:var(--muted)}
.view-all{text-align:right;font-size:6px;color:var(--muted)}
.tags{display:flex;flex-wrap:wrap;gap:4px}
.tags span{border:1px solid var(--line);font-size:6px;padding:2px 5px;color:#666}

/* main */
.main{position:absolute;left:186px;top:136px;width:559px}
.hero{height:126px;position:relative;overflow:hidden;background:linear-gradient(90deg,#e9e4da 0%,#f7f5f0 35%,#fbfaf7 100%)}
.hero .art{position:absolute;left:0;top:0;width:180px;height:100%;background:linear-gradient(90deg,#d9cdb8,#efe9de 90%,transparent)}
.hero h2{position:absolute;left:230px;top:34px;font-size:19px;font-weight:400;color:#555}
.hero h2 .g{color:var(--green);font-weight:700}
.hero h2 .o{color:var(--orange);font-weight:700}
.hero p{position:absolute;left:268px;top:62px;font-size:6.5px;color:var(--muted);text-align:center}
.hero .btn{position:absolute;left:356px;top:82px;background:var(--gold);color:#fff;font-size:6.5px;font-weight:700;padding:3px 10px}
.intro{font-size:6.5px;line-height:1.5;color:#666;margin-top:8px;height:34px}
.toolbar{height:18px;border:1px solid var(--line);display:flex;align-items:center;font-size:6.5px;color:#666;padding:0 6px;gap:6px}
.toolbar .sp{flex:1}
.toolbar .box{border:1px solid var(--line);padding:1px 6px}
.grid{display:grid;grid-template-columns:repeat(4,1fr);column-gap:10px;row-gap:0;margin-top:8px}
.card{height:205px;position:relative}
.card .shot{height:140px;border:1px solid #f0f0f0;position:relative;background:linear-gradient(180deg,#fafafa 0%,#f0f0f0 100%)}
.card .shot.amber{background:radial-gradient(ellipse 30% 42% at 50% 58%,#8a5431 0%,#b58a6c 55%,#fafafa 100%)}
.card .shot.white{background:radial-gradient(ellipse 34% 42% at 52% 55%,#e2e2e2 0%,#f1e6d8 60%,#fcfcfc 100%)}
.new{position:absolute;right:8px;top:6px;width:22px;height:22px;border-radius:50%;background:var(--green);color:#fff;font-size:6px;font-weight:700;display:flex;align-items:center;justify-content:center}
.sale{position:absolute;left:4px;bottom:4px;color:var(--red);font-size:6px;font-weight:700}
.card h3{font-size:6.5px;font-weight:600;margin-top:6px;color:#444}
.card .price{font-size:8.5px;font-weight:700;color:var(--ink);margin-top:3px}
.card .stars{color:var(--gold);font-size:7px;letter-spacing:1px;margin-top:2px}
.card .stars i{color:#ddd;font-style:normal}
</style>
</head>
<body>

<div class="topbar">
  <div>EUR ▾ &nbsp;|&nbsp; FRENCH ▾</div>
  <div class="links"><span>WELCOME GUEST</span><span>MY ACCOUNT</span><span>MY WISHLIST</span><span>MY CART</span><span>CHECKOUT</span><span>LOGIN</span></div>
</div>

<header class="header">
  <div class="brand"><span class="brand-dot"></span><span class="brand-name">Lumea</span></div>
  <div class="shipping">
    <svg width="16" height="12" viewBox="0 0 16 12"><rect x="0" y="2" width="10" height="7" fill="#f5b800"/><path d="M10 4h3l3 3v2h-6z" fill="#f5b800"/><circle cx="3" cy="10" r="1.6" fill="#333"/><circle cx="12" cy="10" r="1.6" fill="#333"/></svg>
    <b>FREE SHIPPING ON ALL ORDER</b>
    <small>Making life better through health and wellbeing</small>
  </div>
  <div class="search"><span>Search entire store here...</span><i><svg width="8" height="8" viewBox="0 0 10 10"><circle cx="4" cy="4" r="3" fill="none" stroke="#fff" stroke-width="1.5"/><path d="M6.5 6.5L9.5 9.5" stroke="#fff" stroke-width="1.5"/></svg></i></div>
</header>

<nav class="nav">
  <div class="cat-btn">CATEGORIES <span>▾</span></div>
  <div class="menu"><a>HOME</a><a>ABOUT US</a><a>CONTACT US</a><a>BRANDS</a><a>RETURNS</a></div>
  <div class="cart"><svg width="10" height="9" viewBox="0 0 10 9"><path d="M0 1h2l1.5 5h5L10 2H3" fill="none" stroke="#333"/><circle cx="4" cy="8" r="1" fill="#333"/><circle cx="8" cy="8" r="1" fill="#333"/></svg>0 Item(s) - $0.00</div>
</nav>

<aside class="sidebar">
  <ul class="cat-list">
    <li>Eye &amp; Sunskins</li><li>Natural Organic</li><li>Health Care</li><li>Personal Care</li><li>Diabetes</li><li>Tablets</li><li>Health Shrubs</li><li>Health Capsules</li>
  </ul>

  <div class="shop-by">
    <div class="block-title">SHOP BY</div>
    <h5>Category</h5>
    <p>Ayurvedic Balms (3)</p><p>Natural Balms (4)</p><p>Healthcare Balms (3)</p>
    <h5>Price</h5>
    <p>$0.00 - $99.99 (5)</p><p>$100.00 and above (5)</p>
  </div>

  <div class="promo">
    <div class="art" role="img" aria-label="Photo of fresh eggs for skin lightening range"></div>
    <h4>Skin Lightening</h4>
    <p>Gentle brightening care for an even, radiant glow every day.</p>
  </div>

  <div class="block">
    <div class="block-title">POPULAR PRODUCTS</div>
    <div class="mini"><div class="thumb amber" role="img" aria-label="Product photo"></div><div><b>Hazelbalm Boost</b><em>$90.00</em><small>Add to Cart</small></div></div>
    <div class="mini"><div class="thumb" role="img" aria-label="Product photo"></div><div><b>Hazelbalm Shine</b><em>$44.00</em><small>Add to Cart</small></div></div>
    <div class="mini"><div class="thumb amber" role="img" aria-label="Product photo"></div><div><b>Hazelnut Power Protect</b><em>$55.00</em><small>Add to Cart</small></div></div>
    <div class="view-all">View All</div>
  </div>

  <div class="block">
    <div class="block-title">POPULAR TAGS</div>
    <div class="tags"><span>Balm</span><span>Herbal</span><span>Natural</span><span>Organic</span><span>Serum</span><span>Vitamins</span><span>Capsule</span><span>Cream</span><span>Care</span><span>Tonic</span></div>
    <div class="view-all" style="margin-top:6px">View All Tags</div>
  </div>

  <div class="block">
    <div class="block-title">SPECIAL PRODUCTS</div>
    <div class="mini"><div class="thumb amber" role="img" aria-label="Product photo"></div><div><b>Daily Herbal Drops</b><em>$60.00</em><small>Add to Cart</small></div></div>
  </div>
</aside>

<main class="main">
  <section class="hero">
    <div class="art" role="img" aria-label="Herbs, mortar and natural remedies photo"></div>
    <h2>Your <span class="g">HEALTH</span> Is Our <span class="o">PASSION</span></h2>
    <p>Making the difference in improving Life, Health and Wellbeing</p>
    <span class="btn">SHOP NOW</span>
  </section>

  <p class="intro">Pure gentle care for every skin, made with natural extracts and calm, trusted ingredients. Our range blends herbal science with daily wellness so you can look and feel your best at every age, morning to night, all year round with simple and honest care.</p>

  <div class="toolbar">
    <span>Items 1 to 16 of 30 total</span><span class="sp"></span>
    <span>Sort By</span><span class="box">Position ▾</span>
    <span>Show</span><span class="box">16 ▾</span><span>per page</span>
    <span class="box">1</span><span class="box">2</span>
  </div>

  <div class="grid">
    <div class="card"><div class="shot amber" role="img" aria-label="Product photo: amber glass supplement bottle"><span class="new">NEW</span><span class="sale">SALE</span></div><h3>Hazelbalm Boost</h3><div class="price">$90.00</div><div class="stars">★★★★<i>★</i></div></div>
    <div class="card"><div class="shot white" role="img" aria-label="Product photo: white bottle with orange gift tag"></div><h3>Hazelbalm Shine</h3><div class="price">$44.00</div><div class="stars">★★★<i>★★</i></div></div>
    <div class="card"><div class="shot amber" role="img" aria-label="Product photo: amber glass supplement bottle"></div><h3>Hazelnut Power Plus</h3><div class="price">$55.00</div><div class="stars">★★★★<i>★</i></div></div>
    <div class="card"><div class="shot white" role="img" aria-label="Product photo: white bottle with orange gift tag"></div><h3>Restore Herbal Balm</h3><div class="price">$130.00</div><div class="stars">★★★★★</div></div>

    <div class="card"><div class="shot white" role="img" aria-label="Product photo: white supplement bottle"></div><h3>Skinwell Protein</h3><div class="price">$120.00</div><div class="stars">★★★<i>★★</i></div></div>
    <div class="card"><div class="shot white" role="img" aria-label="Product photo: white bottle with orange gift tag"></div><h3>Verdalis Protein</h3><div class="price">$95.00</div><div class="stars">★★★★<i>★</i></div></div>
    <div class="card"><div class="shot white" role="img" aria-label="Product photo: white supplement bottle"></div><h3>Clearskin Shake Mix</h3><div class="price">$65.00</div><div class="stars">★★★<i>★★</i></div></div>
    <div class="card"><div class="shot amber" role="img" aria-label="Product photo: amber glass supplement bottle"></div><h3>Nourish Womens Blend</h3><div class="price">$80.00</div><div class="stars">★★★★<i>★</i></div></div>

    <div class="card"><div class="shot amber" role="img" aria-label="Product photo: amber glass supplement bottle"><span class="sale">SALE</span></div><h3>Mobile Nutrition Co</h3><div class="price">$120.00</div><div class="stars">★★★★<i>★</i></div></div>
    <div class="card"><div class="shot amber" role="img" aria-label="Product photo: amber glass supplement bottle"></div><h3>Herbal Protein Shake</h3><div class="price">$95.00</div><div class="stars">★★★<i>★★</i></div></div>
    <div class="card"><div class="shot white" role="img" aria-label="Product photo: white bottle with orange gift tag"></div><h3>Calm Sleep Tonic</h3><div class="price">$65.00</div><div class="stars">★★★★<i>★</i></div></div>
    <div class="card"><div class="shot amber" role="img" aria-label="Product photo: amber glass supplement bottle"></div><h3>Radiance Organic</h3><div class="price">$80.00</div><div class="stars">★★★★★</div></div>

    <div class="card"><div class="shot amber" role="img" aria-label="Product photo: amber glass supplement bottle"><span class="new">NEW</span></div><h3>Weekly Vitamin Glow Balm</h3><div class="price">$90.00</div><div class="stars">★★★★<i>★</i></div></div>
    <div class="card"><div class="shot white" role="img" aria-label="Product photo: white bottle with orange gift tag"></div><h3>Aromatic Flower Blends</h3><div class="price">$44.00</div><div class="stars">★★★<i>★★</i></div></div>
    <div class="card"><div class="shot white" role="img" aria-label="Product photo: white supplement bottle"></div><h3>Health Energy Shots</h3><div class="price">$55.00</div><div class="stars">★★★★<i>★</i></div></div>
    <div class="card"><div class="shot amber" role="img" aria-label="Product photo: amber glass supplement bottle"><span class="new">NEW</span></div><h3>Pure Skin Sprouts</h3><div class="price">$130.00</div><div class="stars">★★★★★</div></div>
  </div>
</main>

</body>
</html>
```